Organic Infographic – "The 4 Dimensions of Transformation"

Overview:
We are a coaching/education brand (Brightmoor Institute) and need a redesigned infographic illustrating our 4-area transformation model. Our current version (attached) uses a rigid, hard-edged triangle/pyramid layout — we want a completely new visual approach that feels organic, soft, and alive, since the topic is human personal development, not a technical process.

Content structure (please keep the wording, redesign the visual form):

4 areas: "Embodiment – The Foundation" and "Focus & Intuition Redefined – The Lens" sit on the same base level. "Heart Centered Living – The Bridge" sits one level above, connecting/enabling the other two. "Becoming Unlimited – The Peak" sits at the top, made possible by Heart Centered Living.
The 4 areas influence and inspire one another — this mutual connection must be visually recognizable (e.g. through overlapping zones, blended color transitions, connecting flowing lines, or similar). Areas may stay visually distinct; the connection between them is what must be shown.
Hierarchy should be expressed mainly through position/arrangement (ascending flow), not through size differences — all 4 areas should carry similar visual weight, since each is equally essential.
A supporting element: "The Brightmoor Methodology" with 3 phases (Phase 1: Awareness & Insight, Phase 2: Integration & Practice, Phase 3: Expansion & Sustainable Growth), each with a short description (text provided below).

Style direction:
Organic, soft, flowing shapes — no sharp angles or rigid geometric triangles. Attached are 3 moodboard references showing the direction we like: overlapping/blended circular shapes, flowing ribbon-style connections, and organic swirl divisions. Please don't copy any of them directly — combine this organic/overlapping visual language with our specific asymmetric hierarchy (2 areas base level + 1 bridge + 1 peak), which none of the references show exactly. This creative translation is the core task.

Icons: Please design one new, unified icon per area (4 total) plus 3 simple icons for the methodology phases — consistent style across all 7, your creative interpretation is welcome.

Typography: Headlines in Arsenal, body text in DM Sans.

Colors: Base palette — Embodiment D09176, Focus & Intuition Redefined B6623E, Heart Centered Living D9866B, Becoming Unlimited 6F7A70, dark text 23211A, light accent EACEC1. Slight adjustments are welcome if they improve visual distinction between areas.

Technical requirements (important):

Final files as vector format (SVG, AI, or EPS), with separated, editable, non-flattened/non-merged layers and paths.
Shapes should consist of simple, closed outline paths — no fine textures, no complex multi-stop gradients, no photorealistic rendering — since the artwork will later be manually redrawn as a whiteboard-animation video.
Primary format: 16:9 landscape. A secondary vertical/mobile version (3 outer areas stacked below the top area) is welcome but optional.

Usage rights: Full commercial usage across website, video, and social media required.

Attachments to include: current draft PDF (for text content and logo reference only — not for layout), our logo file, and the 3 moodboard reference images.

Budget: $100–150 — please let us know if this realistically allows for more designer participation, or advise on adjusting scope/budget

Methodology phase texts (for the 3 supporting icons):

Phase 1: Awareness & Insight
Cultivating self-reflection, identifying patterns, and gaining clarity on personal drivers through introspective practices and data-informed assessment.

Phase 2: Integration & Practice
Applying tools and frameworks, developing new habits, and aligning actions with core values through consistent application and feedback loops.

Phase 3: Expansion & Sustainable Growth
Achieving long-term transformation, exceeding limitations, and fostering resilience through continuous evolution and a purpose-driven approach.

```html
<!DOCTYPE html>
<html lang="en">
<head>
<meta charset="utf-8">
<title>The 4 Dimensions of Transformation – Brightmoor Institute</title>
<link href="https://fonts.googleapis.com/css2?family=Montserrat:ital,wght@0,300;0,400;0,500;0,600;0,700;1,700;1,800&display=swap" rel="stylesheet">
<style>
  :root {
    --backdrop: #6e6f73;
    --paper: #ffffff;
    --ink: #23211a;
    --peak: #6f7a70;
    --peak-light: #c9cfc9;
    --bridge: #e2775a;
    --foundation: #d09176;
    --lens: #b6623e;
    --accent-light: #eacec1;
    --logo-grey: #8b8b8b;
  }
  html, body {
    margin: 0;
    padding: 0;
    width: 1200px;
    height: 2405px;
    overflow: hidden;
    background: var(--backdrop);
    font-family: "Montserrat", sans-serif;
  }
  .asset-library { position: absolute; width: 0; height: 0; overflow: hidden; }
  .artboard {
    position: absolute;
    background: var(--paper);
    box-shadow: 0 30px 40px -20px rgba(0,0,0,0.45);
  }
  .artboard svg { display: block; width: 100%; height: 100%; }
  .artboard--landscape { left: 55px; top: 70px; width: 1090px; height: 613px; }
  .artboard--portrait { left: 220px; top: 800px; width: 760px; height: 1351px; }
  .title-text { font-family: "Montserrat", sans-serif; font-weight: 800; font-style: italic; fill: var(--ink); }
  .brand-name { font-family: "Montserrat", sans-serif; font-weight: 300; fill: var(--logo-grey); }
</style>
</head>
<body>

<svg class="asset-library" aria-hidden="true">
  <defs>
    <linearGradient id="base-band" x1="0" x2="1" y1="0" y2="0">
      <stop offset="0" stop-color="#d09176"/>
      <stop offset="1" stop-color="#b6623e"/>
    </linearGradient>
    <radialGradient id="bridge-glow" cx="0.5" cy="0.5" r="0.5">
      <stop offset="0" stop-color="#ef8a6c"/>
      <stop offset="1" stop-color="#e06f52"/>
    </radialGradient>
    <linearGradient id="title-band" x1="0" x2="1">
      <stop offset="0" stop-color="#f6e8e2"/>
      <stop offset="1" stop-color="#d8937a"/>
    </linearGradient>
    <linearGradient id="card-green" x1="0" x2="1">
      <stop offset="0" stop-color="#9aa39b"/>
      <stop offset="1" stop-color="#ffffff" stop-opacity="0"/>
    </linearGradient>
    <linearGradient id="card-coral" x1="0" x2="1">
      <stop offset="0" stop-color="#f3ddd3"/>
      <stop offset="1" stop-color="#e0876a"/>
    </linearGradient>
    <linearGradient id="card-coral-fade" x1="0" x2="1">
      <stop offset="0" stop-color="#d9866b"/>
      <stop offset="1" stop-color="#ffffff" stop-opacity="0"/>
    </linearGradient>

    <!-- Four-area model -->
    <symbol id="dimension-model" viewBox="0 0 500 430">
      <!-- flowing side ribbons -->
      <path d="M182,95 C150,240 70,190 10,315" fill="none" stroke="#b9bfb8" stroke-width="9" stroke-linecap="round"/>
      <path d="M318,95 C350,240 430,190 490,315" fill="none" stroke="#b9bfb8" stroke-width="9" stroke-linecap="round"/>
      <path d="M170,95 C138,250 50,200 2,330" fill="none" stroke="#c9765a" stroke-width="1.2"/>
      <path d="M330,95 C362,250 450,200 498,330" fill="none" stroke="#c9765a" stroke-width="1.2"/>

      <!-- soft halos -->
      <circle cx="250" cy="82" r="80" fill="var(--peak-light)"/>
      <circle cx="100" cy="320" r="100" fill="#f3e0d8" stroke="#c9765a" stroke-width="1.2"/>
      <circle cx="400" cy="320" r="100" fill="#f3e0d8" stroke="#c9765a" stroke-width="1.2"/>
      <path d="M100,222 C175,222 190,180 250,180 C310,180 325,222 400,222 L400,418 C330,418 310,372 250,372 C190,372 170,418 100,418 Z" fill="#f3e0d8"/>

      <!-- top area + neck -->
      <rect x="208" y="80" width="84" height="110" fill="var(--peak)"/>
      <circle cx="250" cy="82" r="68" fill="var(--peak)"/>

      <!-- base areas joined by band -->
      <path d="M100,232 C172,232 188,196 250,196 C312,196 328,232 400,232 L400,408 C330,408 310,362 250,362 C190,362 170,408 100,408 Z" fill="url(#base-band)"/>
      <circle cx="100" cy="320" r="88" fill="var(--foundation)"/>
      <circle cx="400" cy="320" r="88" fill="var(--lens)"/>
      <path d="M140,392 C200,350 300,350 360,392" fill="none" stroke="#ffffff" stroke-opacity="0.6" stroke-width="5" stroke-linecap="round"/>

      <!-- bridge -->
      <circle cx="250" cy="212" r="90" fill="#f1b7a3" fill-opacity="0.55"/>
      <circle cx="250" cy="212" r="78" fill="url(#bridge-glow)"/>

      <!-- icons -->
      <g fill="none" stroke="#ffffff" stroke-width="1.6" stroke-linecap="round">
        <!-- peak: rising burst -->
        <g transform="translate(250,42)">
          <circle r="5"/>
          <path d="M0,-18 V-9 M0,9 V18 M-18,0 H-9 M9,0 H18 M-13,-13 L-7,-7 M13,-13 L7,-7 M-13,13 L-7,7 M13,13 L7,7"/>
        </g>
        <!-- bridge: heart with nodes -->
        <g transform="translate(250,178)">
          <path d="M0,10 C-14,0 -12,-10 -6,-10 C-3,-10 -1,-8 0,-5 C1,-8 3,-10 6,-10 C12,-10 14,0 0,10 Z"/>
          <path d="M-10,-10 L-16,-17 M10,-10 L16,-17 M0,-10 V-20 M-14,4 L-22,6 M14,4 L22,6"/>
          <circle cx="-17" cy="-18" r="2"/><circle cx="17" cy="-18" r="2"/><circle cx="0" cy="-22" r="2"/>
          <circle cx="-24" cy="6" r="2"/><circle cx="24" cy="6" r="2"/>
        </g>
        <!-- foundation: grounded globe -->
        <g transform="translate(100,292)">
          <circle r="15"/>
          <path d="M-15,0 H15 M0,-15 C-8,-6 -8,6 0,15 M0,-15 C8,-6 8,6 0,15 M-20,20 H20"/>
        </g>
        <!-- lens: eye with rings -->
        <g transform="translate(400,278)">
          <path d="M-16,0 C-8,-10 8,-10 16,0 C8,10 -8,10 -16,0 Z"/>
          <circle r="4"/>
          <path d="M-12,-14 C-4,-20 4,-20 12,-14 M-12,14 C-4,20 4,20 12,14"/>
        </g>
      </g>

      <!-- labels -->
      <g font-family="Montserrat, sans-serif" fill="#ffffff" text-anchor="middle">
        <text x="250" y="82" font-size="14" font-weight="600">Becoming</text>
        <text x="250" y="98" font-size="14" font-weight="600">Unlimited</text>
        <text x="250" y="116" font-size="9" font-weight="400" fill-opacity="0.85">The Peak</text>

        <text x="250" y="222" font-size="14" font-weight="500">Heart Centered</text>
        <text x="250" y="238" font-size="14" font-weight="500">Living</text>
        <text x="250" y="258" font-size="9" font-weight="400" fill-opacity="0.85">The Bridge</text>

        <text x="95" y="336" font-size="14" font-weight="600">Embodiment</text>
        <text x="95" y="354" font-size="9" font-weight="400" fill-opacity="0.85">The Foundation</text>

        <text x="395" y="318" font-size="14" font-weight="500">Focus &amp; Intuition</text>
        <text x="395" y="334" font-size="14" font-weight="500">Redefined</text>
        <text x="395" y="354" font-size="9" font-weight="400" fill-opacity="0.85">The Lens</text>
      </g>
    </symbol>

    <!-- Phase 1 -->
    <symbol id="phase-awareness" viewBox="0 0 330 120">
      <path d="M80,6 H60 A54,54 0 0 0 60,114 H200" fill="none" stroke="#9aa39b" stroke-width="1.2"/>
      <rect x="12" y="12" width="290" height="96" rx="48" fill="url(#card-green)"/>
      <circle cx="60" cy="60" r="40" fill="var(--peak)"/>
      <g fill="none" stroke="#ffffff" stroke-width="1.5" stroke-linecap="round">
        <path d="M53,72 C46,66 44,60 44,55 A16,16 0 0 1 76,55 C76,60 74,66 67,72 Z"/>
        <path d="M53,77 H67 M55,82 H65"/>
        <circle cx="60" cy="55" r="5" stroke-dasharray="3 2"/>
        <path d="M60,32 V28 M40,40 L37,37 M80,40 L83,37 M35,56 H31 M85,56 H89"/>
      </g>
      <g font-family="Montserrat, sans-serif">
        <text x="112" y="30" font-size="14" font-weight="800" font-style="italic" fill="#7f8a80">PHASE <tspan font-size="26">1</tspan></text>
        <text x="112" y="45" font-size="10" font-weight="700" fill="#23211a">Awareness &amp; Insight</text>
        <g font-size="8.4" fill="#23211a">
          <text x="112" y="58">Cultivating self-reflection, identifying</text>
          <text x="112" y="69">patterns, and gaining clarity on personal</text>
          <text x="112" y="80">drivers through introspective practices and</text>
          <text x="112" y="91">data-informed assessment.</text>
        </g>
      </g>
    </symbol>

    <!-- Phase 2 -->
    <symbol id="phase-integration" viewBox="0 0 330 120">
      <path d="M130,6 H270 A54,54 0 0 1 270,114 H230" fill="none" stroke="#c9765a" stroke-width="1.2"/>
      <rect x="28" y="12" width="290" height="96" rx="48" fill="url(#card-coral)"/>
      <circle cx="60" cy="60" r="36" fill="#e07a5c"/>
      <g fill="none" stroke="#ffffff" stroke-width="1.5" stroke-linecap="round">
        <circle cx="62" cy="60" r="14" stroke-dasharray="4 3"/>
        <circle cx="62" cy="60" r="6"/>
        <path d="M38,52 H48 M36,60 H48 M38,68 H48"/>
      </g>
      <g font-family="Montserrat, sans-serif">
        <text x="112" y="30" font-size="14" font-weight="800" font-style="italic" fill="#d9694a">PHASE <tspan font-size="26">2</tspan></text>
        <text x="112" y="45" font-size="10" font-weight="700" fill="#23211a">Integration &amp; Practice</text>
        <g font-size="8.4" fill="#23211a">
          <text x="112" y="58">Applying tools and frameworks, developing</text>
          <text x="112" y="69">new habits, and aligning actions with core</text>
          <text x="112" y="80">values through consistent application</text>
          <text x="112" y="91">and feedback loops.</text>
        </g>
      </g>
    </symbol>

    <!-- Phase 3 -->
    <symbol id="phase-expansion" viewBox="0 0 330 120">
      <path d="M80,6 H60 A54,54 0 0 0 60,114 H200" fill="none" stroke="#c9765a" stroke-width="1.2"/>
      <rect x="12" y="12" width="300" height="96" rx="48" fill="url(#card-coral-fade)" fill-opacity="0.7"/>
      <circle cx="60" cy="60" r="40" fill="#c9684a"/>
      <g fill="none" stroke="#ffffff" stroke-width="1.5" stroke-linecap="round" stroke-linejoin="round">
        <rect x="44" y="66" width="6" height="12"/>
        <rect x="54" y="60" width="6" height="18"/>
        <rect x="64" y="54" width="6" height="24"/>
        <path d="M42,58 L54,48 L62,52 L76,40 M70,40 H76 V46"/>
      </g>
      <g font-family="Montserrat, sans-serif">
        <text x="112" y="30" font-size="14" font-weight="800" font-style="italic" fill="#d9694a">PHASE <tspan font-size="26">3</tspan></text>
        <text x="112" y="45" font-size="10" font-weight="700" fill="#23211a">Expansion &amp; Sustainable Growth</text>
        <g font-size="8.4" fill="#23211a">
          <text x="112" y="58">Achieving long-term transformation,</text>
          <text x="112" y="69">exceeding limitations, and fostering resilience</text>
          <text x="112" y="80">through continuous evolution and a</text>
          <text x="112" y="91">purpose-driven approach.</text>
        </g>
      </g>
    </symbol>
  </defs>
</svg>

<!-- Landscape 16:9 -->
<section class="artboard artboard--landscape" aria-label="The 4 Dimensions of Transformation, landscape">
  <svg viewBox="0 0 1000 562">
    <g class="title-band">
      <path d="M0,25 H597 A26,26 0 0 1 597,77 H0 Z" fill="url(#title-band)"/>
      <text class="title-text" x="35" y="61" font-size="28">The 4 Dimensions of  Transformation</text>
    </g>
    <g class="brand">
      <circle cx="658" cy="51" r="22" fill="#d9866b"/>
      <text class="brand-name" x="690" y="62" font-size="29">Brightmoor Institute</text>
    </g>
    <use href="#dimension-model" x="40" y="115" width="500" height="430"/>
    <use href="#phase-awareness" x="598" y="115" width="330" height="120"/>
    <use href="#phase-integration" x="598" y="250" width="330" height="120"/>
    <use href="#phase-expansion" x="598" y="385" width="330" height="120"/>
  </svg>
</section>

<!-- Portrait version -->
<section class="artboard artboard--portrait" aria-label="The 4 Dimensions of Transformation, portrait">
  <svg viewBox="0 0 750 1333">
    <g class="brand">
      <circle cx="200" cy="78" r="34" fill="#d9866b"/>
      <text class="brand-name" x="248" y="94" font-size="44">Brightmoor Institute</text>
    </g>
    <g class="title-band">
      <path d="M40,145 H700 A28,28 0 0 1 700,201 H40 Z" fill="url(#title-band)"/>
      <text class="title-text" x="58" y="186" font-size="34">The 4 Dimensions of  Transformation</text>
    </g>
    <use href="#dimension-model" x="75" y="230" width="600" height="516"/>
    <use href="#phase-awareness" x="160" y="765" width="450" height="164"/>
    <use href="#phase-integration" x="160" y="945" width="450" height="164"/>
    <use href="#phase-expansion" x="160" y="1125" width="450" height="164"/>
  </svg>
</section>

</body>
</html>
```